Website Redesign for a faith-based, not-for-profit health and human services organization

New website design for the Hearthside Faith Outreach House.
- Current site: www.hfohtr.org -
We are looking for a nice clean, simple, friendly-yet-elegant website layout.
Colors are #f5eed5 (cream), #FFFFFF (white), and all logo colors.
Design a layout for home page
Design a layout for general layouts
-layout only no html needed (preferably a high res PSD file format) -
Main menu should be along top with side navigation for submenu, no side menu on home page.
Also would be open to seeing some updated colors on the logo design, currently the colors are slightly outdated. The Vine of Plenty quilt design fits the organization’s mission and the rural farming / Amish-Mennonite-Brethren community around us.

ADDITIONAL PAGES AND MENU STRUCTURE ON NEW SITE

- How to Help
... Volunteer
... Donate Time
... Donate Money
... Donate Supplies
... Current Needs

- Programs

- News & Events
... Upcoming Events
... Upcoming Fundraisers
... Newsletter

- Our Partners

- About Us
... Overview
... Mission
... Staff Directory
... Board of Directors
... Annual Reports

- Contact

Our annual special event is Gather at the Hearth and should be integrated into the home page - see attached logos and banner

Websites with elements we like (from organizations doing similar work), each for a different reason....

1. http://www.kinbridgeway.org
Good design, color, clarity on this site. Multi-dimensional, photos...easy interaction, etc.

2. http://endfamineplainly.org
Quite simple, nothing fancy, but some good basic stuff here, and pretty easy to navigate...

3. http://www.neighborhub.org
Intrigued by the bulletin board design and the way they have their programs broken down to show impact, needs, etc. It has a lot of good information, but is really too verbose, some of the print is too small, etc. Not perfect, but some interesting design elements.

4. http://sharedlarder.org
Site is boring and not very well designed, but it has some of the features that we would like to see at the top, donations, partners, etc.

5. http://www.meadowlarkgrocers.org
Too many listings on the sidebar - needs to be cleaner & simpler, but a lot of good information and we like the way they show volunteer photos on the Our Helpers Shine Bright page...

About
Hearthside Faith Outreach House ("HFOH" or “the Center”) is a faith-based non-for-profit health and human services organization that exists as an outreach of and for the Ostrel Valley Unified School District.
Tagline: Mercy at Work (we work to serve the needs of the ‘least of these’ with compassion).

Mission
Our mission is to see lives transformed and the community enhanced by encouraging the oppressed, defending the cause of the weak and maintaining the rights of the poor - bringing together the resources of a caring community as a demonstration of the good news of Christ.

Company Overview
Hearthside Faith Outreach House works closely with the community in which it serves. A tremendous value is placed upon the partnerships that have formed with caring people within the community and with organizations that share the goal of bringing together resources to help those who need it most. Individuals, volunteers, churches, corporations, foundations, and government sources all pull together to help make our mission possible.

Since 1996 the Hearthside Faith Outreach House has collaboratively worked to see our community enhanced, adapting programs and services to meet the changing needs of the community.

Target Market(s)

people needing assistance in local community

Industry/Entity Type

Government

Requirements
Must have
• Good social button integration
Should not have
• No Find Us page like old website it is not needed

```html
<!DOCTYPE html>
<html lang="en">
<head>
<meta charset="utf-8">
<title>Hearthside Faith Outreach House</title>
<link rel="stylesheet" href="https://fonts.googleapis.com/css2?family=Noto+Serif:ital,wght@0,400;0,700;1,700&display=swap">
<style>
  :root {
    --wood-light: #eeeae0;
    --wood-dark: #ddd6c6;
    --cream: #f5eed5;
    --white: #ffffff;
    --berry: #7d1a2b;
    --berry-dark: #5e1220;
    --forest: #1d4a27;
    --gold: #c9a13a;
    --ink: #2a2a2a;
    --rule: #d9c9a0;
  }
  * { box-sizing: border-box; margin: 0; padding: 0; }
  html, body { width: 847px; height: 1200px; overflow: hidden; }
  body {
    position: relative;
    font-family: "Noto Serif", Georgia, serif;
    color: var(--ink);
    background: repeating-linear-gradient(90deg, var(--wood-light) 0 60px, var(--wood-dark) 60px 62px, var(--wood-light) 62px 120px);
  }
  .page {
    position: absolute; left: 92px; top: 22px; width: 663px; height: 1165px;
    background: var(--white); box-shadow: 0 0 8px rgba(0,0,0,.25);
  }
  .top-bar { position: absolute; left: 0; top: 0; width: 100%; height: 8px; background: var(--forest); }
  .brand { position: absolute; left: 24px; top: 24px; display: flex; align-items: center; gap: 10px; }
  .brand-mark { width: 26px; height: 26px; background: var(--berry); }
  .brand-name { font-size: 16px; line-height: 17px; color: var(--gold); width: 150px; }
  .social { position: absolute; right: 42px; top: 46px; display: flex; gap: 20px; }
  .social-item { display: flex; flex-direction: column; align-items: center; font-size: 8.5px; font-weight: 700; font-style: italic; color: var(--forest); }
  .social-item .dot { width: 22px; height: 22px; border-radius: 50%; background: var(--forest); margin-bottom: 3px; }
  .ribbon { position: absolute; left: -36px; top: 105px; width: 735px; height: 45px; }
  .nav { position: absolute; left: 0; top: 105px; width: 663px; height: 45px; background: var(--berry); }
  .nav a { position: absolute; top: 13px; font-size: 14px; letter-spacing: -0.3px; white-space: nowrap; color: var(--white); text-decoration: none; }
  .nav a.current { text-decoration: underline; }
  .hero { position: absolute; left: 0; top: 150px; width: 663px; height: 231px; background: linear-gradient(135deg, #8a7a62, #c96a2a 45%, #a44a2a 70%, #6b5a48); }
  .hero-caption { position: absolute; left: 0; bottom: 0; width: 100%; height: 43px; background: rgba(30,28,26,.85); color: var(--white); font-size: 12.6px; letter-spacing: -0.3px; white-space: nowrap; line-height: 43px; text-align: center; }
  .hero-line { position: absolute; left: 0; top: 381px; width: 663px; height: 2px; background: var(--berry); }
  .dropdown { position: absolute; left: 83px; top: 142px; width: 130px; background: var(--white); box-shadow: 0 1px 4px rgba(0,0,0,.3); padding: 3px 0; list-style: none; }
  .dropdown li { font-size: 11.5px; padding: 0 8px; height: 24px; line-height: 24px; border-bottom: 1px solid #e6e0d0; white-space: nowrap; }
  .dropdown li:last-child { border-bottom: 0; }
  .dropdown li.active { color: var(--gold); }
  .rule { position: absolute; left: 23px; width: 596px; height: 1px; background: var(--rule); }
  .col { position: absolute; top: 414px; width: 305px; }
  .col h2 { font-size: 19.5px; letter-spacing: -0.3px; white-space: nowrap; color: var(--berry); font-weight: 700; line-height: 26px; height: 30px; }
  .photo { width: 303px; height: 122px; margin-top: 1px; }
  .col p { margin-top: 14px; font-size: 11.2px; letter-spacing: -0.15px; line-height: 21px; }
  .col p strong { color: var(--forest); }
  .btn { position: absolute; background: var(--forest); color: var(--white); font-size: 11.5px; text-align: center; line-height: 25px; height: 25px; box-shadow: 0 0 0 2px #cfd8cf; }
  .verse { position: absolute; left: 0; top: 763px; width: 663px; height: 103px; background: var(--cream); text-align: center; padding: 14px 22px 0; }
  .verse h3 { font-size: 20px; color: var(--berry); line-height: 26px; }
  .verse p { font-size: 10.6px; letter-spacing: -0.1px; line-height: 16.6px; margin-top: 5px; }
  .poster { position: absolute; left: 20px; top: 908px; width: 134px; height: 210px; background: linear-gradient(160deg, #5d7a2e, #d7d84a 40%, #c9cc3c); }
  .event { position: absolute; left: 169px; top: 902px; width: 455px; }
  .event h2 { font-size: 20.5px; color: var(--berry); line-height: 28px; }
  .event h4 { font-size: 14px; font-weight: 400; color: var(--berry); margin-top: 2px; }
  .event p { font-size: 10.8px; letter-spacing: -0.1px; line-height: 14px; margin-top: 8px; }
  .event p strong { color: var(--forest); }
  .event p a { color: var(--berry); font-weight: 700; font-style: italic; text-decoration: underline; }
  .event-mark { position: absolute; left: 465px; top: 1055px; display: flex; align-items: center; gap: 6px; }
  .event-mark .dot { width: 16px; height: 16px; border-radius: 50%; background: var(--gold); }
  .event-mark span { font-size: 14px; font-weight: 700; color: var(--berry); white-space: nowrap; }
  .footer { position: absolute; left: 0; top: 1141px; width: 663px; height: 24px; background: var(--forest); color: var(--white); font-size: 8.4px; font-weight: 700; line-height: 24px; padding-left: 18px; white-space: nowrap; }
  .footer-icons { position: absolute; left: 358px; top: 4px; display: flex; gap: 8px; }
  .footer-icons i { width: 16px; height: 16px; border-radius: 50%; border: 1.5px solid var(--white); }
</style>
</head>
<body>
  <div class="page">
    <div class="top-bar"></div>
    <div class="brand"><div class="brand-mark"></div><div class="brand-name">Hearthside Faith Outreach House</div></div>
    <div class="social">
      <div class="social-item"><span class="dot"></span>Chatterline</div>
      <div class="social-item"><span class="dot"></span>Neighborbook</div>
      <div class="social-item"><span class="dot"></span>Email</div>
    </div>

    <svg class="ribbon" viewBox="0 0 735 45" aria-hidden="true">
      <polygon points="0,8 36,0 36,45 0,45 12,27" fill="var(--berry-dark)"/>
      <polygon points="735,8 699,0 699,45 735,45 723,27" fill="var(--berry-dark)"/>
    </svg>
    <nav class="nav">
      <a class="current" style="left:22px">Home</a>
      <a style="left:83px">About Us</a>
      <a style="left:166px">How to Help</a>
      <a style="left:267px">Our Partners</a>
      <a style="left:371px">News &amp; Events</a>
      <a style="left:488px">Programs</a>
      <a style="left:572px">Contact</a>
    </nav>

    <div class="hero" role="img" aria-label="Volunteers gathered together in the food pantry">
      <div class="hero-caption">Thank you to Cedar Hollow Farms &amp; everyone who helped make our first Farm-To-Table event a success!</div>
    </div>
    <div class="hero-line"></div>

    <ul class="dropdown">
      <li class="active">Overview</li>
      <li>Mission</li>
      <li>Staff Directory</li>
      <li>Board of Directors</li>
      <li>Annual Reports</li>
    </ul>

    <div class="rule" style="top:401px"></div>

    <section class="col" style="left:23px">
      <h2>Building a Better Community</h2>
      <div class="photo" role="img" aria-label="Group of volunteer women at a community gathering" style="background:linear-gradient(135deg,#7a6a5a,#b24a4a 50%,#3a3a4a)"></div>
      <p><strong>Hearthside Faith Outreach House</strong> works closely with the community in which it serves. A tremendous amount of value is placed upon the partnerships that have formed with caring people within the community and organizations that share the goal of bringing together resources to help those who need it most.</p>
    </section>
    <a class="btn" style="left:224px;top:727px;width:89px">Read More</a>

    <section class="col" style="left:338px">
      <h2>Our Mission</h2>
      <div class="photo" role="img" aria-label="Large group of volunteers in matching white shirts" style="background:linear-gradient(180deg,#7a4a3a,#e8e8ea 55%,#6a7a8a)"></div>
      <p><strong>Our mission</strong> is to see lives transformed and the community enhanced by encouraging the oppressed, defending the cause of the weak and maintaining the rights of the poor by bringing together the resources of a caring community as a demonstration of the good news of Christ.</p>
    </section>
    <a class="btn" style="left:539px;top:704px;width:89px">Read More</a>

    <section class="verse">
      <h3>Ezekiel 47:12</h3>
      <p>“Along the bank of the river, on this side and that, will grow all kinds of trees used for food; their leaves will not wither, and their fruit will not fail. They will bear fruit every month, because their water flows from the sanctuary. Their fruit will be for food, and their leaves for medicine.”</p>
    </section>

    <div class="rule" style="top:889px"></div>

    <div class="poster" role="img" aria-label="Event poster for the second annual farm to table dinner auction"></div>
    <section class="event">
      <h2>Gather at the Hearth</h2>
      <h4>Farm to Table Dinner Auction Event</h4>
      <p><strong>Gather at the Hearth</strong> is a dinner auction event with a goal of engaging the community around us to raise funds in support of HFOH’s mission.&nbsp; Area chefs and farms will come together and donate time, skill and food to prepare a meal, and an evening of fun, for up to 300 guests.&nbsp; <a>Read More</a></p>
    </section>
    <div class="event-mark"><span class="dot"></span><span>Gather at the Hearth</span></div>

    <footer class="footer">Copyright 2013 &nbsp;| &nbsp;Hearthside Faith Outreach House &nbsp;| &nbsp;All Rights Reserved
      <div class="footer-icons"><i></i><i></i><i></i></div>
    </footer>
  </div>
</body>
</html>
```